Wrap needed for mobile fleet washing service

We need a wrap design for the mobile fleet washing division of our company, Brisq. We send crews of guys to our customers' locations to wash their fleet vehicles with pressure washers and chemicals, so they don't have to wash their vehicles themselves. We wash dump trucks, tractor-trailers, and garbage trucks, primarily. The wrap needs to fit a 2017 Dolvo cabover truck with an 18 foot box on it. Wrap needs to be clean, modern, and professional.
Target Market(s)
Businesses with fleets-- hauling companies, garbage companies, trucking companies.
Industry/Entity Type
Service, Transportation

```html
<!DOCTYPE html>
<html lang="en">
<head>
<meta charset="utf-8">
<title>Brisq Fleet Washing – Truck Wrap</title>
<link rel="stylesheet" href="https://fonts.googleapis.com/css2?family=Lexend:wght@500&family=Saira+Semi+Condensed:wght@600&family=Poppins:wght@400;500&display=swap">
<style>
  :root {
    --brand-blue: #1d86c6;
    --ink: #3a3d42;
    --rule: #5d6168;
    --panel: #ffffff;
    --stage: #eceff3;
    --hose-soft: #d6e9f5;
  }
  * { margin: 0; padding: 0; box-sizing: border-box; }
  html, body {
    width: 1200px;
    height: 1200px;
    overflow: hidden;
    background: var(--stage);
  }
  .wrap-layout {
    position: absolute;
    left: 50px;
    top: 410px;
    display: flex;
    gap: 20px;
    align-items: flex-end;
  }
  .box-side {
    position: relative;
    width: 850px;
    height: 380px;
    background: var(--panel);
    box-shadow: 0 2px 10px rgba(0,0,0,.08);
    overflow: hidden;
  }
  .brand-name {
    position: absolute;
    left: 180px;
    top: 16px;
    font-family: "Lexend", sans-serif;
    font-weight: 500;
    font-size: 168px;
    line-height: 1;
    letter-spacing: 8px;
    color: var(--brand-blue);
  }
  .washer-art {
    position: absolute;
    left: 55px;
    top: 228px;
    width: 640px;
    height: 44px;
    background: linear-gradient(90deg, var(--hose-soft), #eaf4fa);
    border-radius: 6px;
  }
  .service-line {
    position: absolute;
    left: 0;
    right: 0;
    top: 288px;
    height: 30px;
    display: flex;
    align-items: center;
    gap: 12px;
    padding: 0 30px;
  }
  .service-line .rule {
    flex: 1;
    min-width: 30px;
    height: 4px;
    background: var(--rule);
  }
  .service-line .services {
    font-family: "Saira Semi Condensed", sans-serif;
    font-weight: 600;
    font-size: 19px;
    line-height: 1;
    letter-spacing: 1.6px;
    color: var(--ink);
    white-space: nowrap;
  }
  .contact-band {
    position: absolute;
    left: 0;
    right: 0;
    top: 324px;
    height: 44px;
    background: var(--brand-blue);
    display: flex;
    align-items: center;
    padding-left: 110px;
    color: #fff;
    font-family: "Poppins", sans-serif;
  }
  .contact-band .phone {
    font-weight: 500;
    font-size: 28px;
    letter-spacing: 2px;
  }
  .contact-band .divider {
    width: 3px;
    height: 28px;
    background: #fff;
    margin: 0 16px;
  }
  .contact-band .web {
    font-weight: 400;
    font-size: 21px;
    letter-spacing: 1.5px;
  }
  .cab-door {
    position: relative;
    width: 230px;
    height: 380px;
    background: var(--panel);
    box-shadow: 0 2px 10px rgba(0,0,0,.08);
    overflow: hidden;
  }
  .cab-door .trim {
    position: absolute;
    left: 0; right: 0;
    top: 168px;
    height: 6px;
    background: var(--ink);
  }
  .cab-door .lower {
    position: absolute;
    left: 0; right: 0;
    top: 180px;
    bottom: 0;
    background: var(--brand-blue);
  }
  .cab-mark {
    position: absolute;
    left: 26px;
    top: 236px;
    display: flex;
    align-items: center;
    color: #fff;
  }
  .cab-mark .name {
    font-family: "Lexend", sans-serif;
    font-weight: 500;
    font-size: 36px;
    line-height: 1;
  }
  .cab-mark .split {
    width: 2px;
    height: 42px;
    background: #fff;
    margin: 0 12px;
  }
  .cab-mark .division {
    font-family: "Poppins", sans-serif;
    font-size: 13px;
    letter-spacing: 1px;
    line-height: 1.5;
  }
</style>
</head>
<body>
  <main class="wrap-layout">
    <section class="box-side" aria-label="Box side wrap">
      <div class="brand-name">Brisq</div>
      <div class="washer-art" role="img" aria-label="Pressure washer wand and hose line illustration"></div>
      <div class="service-line">
        <span class="rule"></span>
        <span class="services">WASH DUMP TRUCKS • TRACTOR-TRAILERS • GARBAGE TRUCKS</span>
        <span class="rule"></span>
      </div>
      <div class="contact-band">
        <span class="phone">142-555-0186</span>
        <span class="divider"></span>
        <span class="web">www.brisqwashing.com</span>
      </div>
    </section>

    <section class="cab-door" aria-label="Cab door wrap">
      <div class="trim"></div>
      <div class="lower"></div>
      <div class="cab-mark">
        <span class="name">Brisq</span>
        <span class="split"></span>
        <span class="division">FLEET<br>WASHING</span>
      </div>
    </section>
  </main>
</body>
</html>
```